Website for Life Strategies business

We need a website to present our video, audio and print content to subcribers at Kindred Ascent Partners. We will offer a team of coaches who can help people breakthrough the barriers that keep them from reaching their physical, spiritual, financial, leadership and relationship goals.

Target Market(s)

Anyone who needs help with strategies to take their life to a new level of success.

Industry/Entity Type

Life Coaching

Logo Text

Kindred Ascent Partners

Number of Pages Required

5+ page

Colors

Designer to choose colors to be used in the design.

Requirements
Must have
• The ability to present content as a package that includes Word Documents, videos and audio content as well as to be able to display books for sale. Each week their would be a new package for subscribers to access. It should provide the ability for subscribers to comment on the material and share how their lives were changed by the content. Should also include a shop page to offer merchandise for sale.
Nice to have
• Not sure
Should not have
• Not sure

```html
<!DOCTYPE html>
<html lang="en">
<head>
<meta charset="utf-8">
<title>Kindred Ascent Partners</title>
<link rel="stylesheet" href="https://fonts.googleapis.com/css2?family=Nunito+Sans:wght@400;600;700;800&family=Open+Sans:wght@400;600;700&display=swap">
<style>
:root{
  --gold:#dba21f;
  --teal:#17a19b;
  --green:#7dbb33;
  --orange:#e9921e;
  --blue:#2f6fb8;
  --red:#e64b4b;
  --ink:#1f1f1f;
  --body:#6d6d6d;
  --muted:#9a9a9a;
  --line:#e4e4e4;
  --white:#ffffff;
}
*{box-sizing:border-box;margin:0;padding:0}
html,body{width:1200px;height:2951px;overflow:hidden;background:var(--white)}
body{font-family:"Open Sans",Arial,sans-serif;color:var(--body);position:relative}
h1,h2,h3,h4,.logo,.nav a,.stat-num{font-family:"Nunito Sans",Arial,sans-serif}

/* hero */
.hero{position:absolute;left:0;top:0;width:1200px;height:560px;
  background:linear-gradient(100deg,#a58a6e 0%,#c9a57e 25%,#e6a661 45%,#d9833a 65%,#c2753a 85%,#9a6a4a 100%)}
.hero-photo{position:absolute;inset:0;background:radial-gradient(ellipse at 55% 35%,rgba(255,220,170,.55),rgba(255,200,140,0) 55%),linear-gradient(180deg,rgba(60,40,30,.15),rgba(0,0,0,0) 30%,rgba(0,0,0,.1))}
.topbar{position:absolute;left:0;top:0;width:1200px;height:88px;border-bottom:1px solid rgba(255,255,255,.3)}
.logo{position:absolute;left:98px;top:24px;color:var(--white);font-weight:700;font-size:19px;letter-spacing:1.5px;width:200px;line-height:22px}
.nav{position:absolute;right:98px;top:34px;display:flex;gap:34px;align-items:center}
.nav a{color:var(--white);text-decoration:none;font-size:14px;font-weight:700}
.nav a.active{color:var(--gold)}
.hero-title{position:absolute;left:0;width:1200px;top:212px;text-align:center;color:var(--white);font-size:52px;font-weight:800;letter-spacing:.5px}
.hero-sub{position:absolute;left:0;width:1200px;top:290px;text-align:center;color:var(--white);font-size:20px;font-weight:600}
.hero-btn{position:absolute;left:502px;top:345px;width:196px;height:42px;border:2px solid var(--white);border-radius:22px;color:var(--white);font-family:"Nunito Sans",sans-serif;font-weight:800;font-size:15px;text-align:center;line-height:38px}
.dots{position:absolute;top:490px;left:562px;display:flex;gap:5px}
.dots span{width:14px;height:14px;border:2px solid var(--white);border-radius:50%}
.dots span.on{background:var(--white)}

/* welcome */
.section-title{position:absolute;left:0;width:1200px;text-align:center;color:var(--ink);font-size:26px;font-weight:700}
.welcome-text{position:absolute;left:210px;width:780px;top:683px;text-align:center;font-size:12.5px;line-height:25px}
.pillar{position:absolute;top:772px;width:220px;text-align:center}
.pillar .ring{width:132px;height:132px;border:2px solid;border-radius:50%;margin:0 auto;display:flex;align-items:center;justify-content:center}
.pillar h3{margin-top:40px;font-size:17px;font-weight:600;color:var(--ink)}
.pillar p{margin-top:14px;font-size:12px;line-height:21px;padding:0 26px}
.pillar .more{display:block;margin-top:12px;font-size:11.5px;font-weight:700}

/* stats */
.stats{position:absolute;left:0;top:1123px;width:1200px;height:317px;background:linear-gradient(100deg,#3a3836 0%,#5d5a56 30%,#8a8379 55%,#b58a5a 75%,#5a4b40 100%)}
.stat{position:absolute;top:50px;width:220px;text-align:center;color:var(--white)}
.stat .ring{width:148px;height:148px;border:3px solid var(--white);border-radius:50%;margin:0 auto;display:flex;align-items:center;justify-content:center}
.stat-num{margin-top:24px;font-size:25px;font-weight:800}
.stat-label{margin-top:4px;font-size:13px;font-weight:700}

/* blog */
.card{position:absolute;width:318px;height:421px;border:1px solid #dcdcdc;box-shadow:0 1px 4px rgba(0,0,0,.12);background:var(--white)}
.card .photo{position:absolute;left:6px;top:6px;width:304px;height:203px}
.card .tag{position:absolute;left:6px;top:6px;background:#222;color:var(--white);font-size:11px;font-weight:700;padding:5px 14px}
.card .play{position:absolute;left:128px;top:79px}
.card .audio{position:absolute;left:188px;top:128px}
.card h4{position:absolute;left:22px;top:233px;font-size:18px;font-weight:700;color:var(--ink)}
.card .meta{position:absolute;left:22px;top:266px;font-size:11.5px;color:#777}
.card .excerpt{position:absolute;left:22px;top:295px;width:280px;font-size:11.5px;line-height:21px}
.card .more{position:absolute;left:22px;top:383px;font-size:11.5px;font-weight:700;color:var(--gold)}
.view-more{position:absolute;left:511px;top:2508px;width:178px;height:48px;border:1px solid #d5d5d5;border-radius:24px;text-align:center;line-height:46px;font-size:13px;font-weight:700;color:var(--gold)}

/* footer */
.footer-rule{position:absolute;left:0;top:2618px;width:1200px;height:4px;background:var(--gold)}
.footer-logo{position:absolute;left:98px;top:2730px;color:var(--ink);font-family:"Nunito Sans",sans-serif;font-weight:700;font-size:21px;letter-spacing:1px;width:210px;line-height:27px}
.fcol{position:absolute;top:2680px}
.fcol h4{font-size:17px;font-weight:700;color:var(--ink);margin-bottom:18px}
.fcol li{list-style:none;font-size:11.5px;color:#555;line-height:28px}
.fcol p{font-size:11.5px;line-height:20px;color:#555}
.field{margin-top:16px;width:256px;height:38px;border:1px solid #d5d5d5;font-size:11px;color:#aaa;padding:11px 12px}
.subscribe{margin-top:16px;width:96px;height:32px;border:1px solid #d5d5d5;border-radius:16px;text-align:center;line-height:30px;font-size:11px;font-weight:700;color:var(--gold)}
.contact-row{display:flex;gap:14px;font-size:11.5px;color:#555;line-height:22px;margin-bottom:18px}
.contact-row svg{flex:none;margin-top:4px}
.footer-bottom{position:absolute;left:98px;top:2876px;width:1004px;border-top:1px solid var(--line)}
.copyright{position:absolute;left:98px;top:2908px;font-size:11.5px;color:#555}
.socials{position:absolute;right:98px;top:2898px;display:flex;gap:10px}
.socials span{width:34px;height:34px;border:1px solid var(--gold);border-radius:50%}
</style>
</head>
<body>

<header class="hero">
  <div class="hero-photo" role="img" aria-label="Photo of a woman with arms spread wide against a warm sunset sky"></div>
  <div class="topbar">
    <div class="logo">Kindred Ascent Partners</div>
    <nav class="nav">
      <a class="active" href="#">HOME</a><a href="#">ABOUT US</a><a href="#">SERVICES</a><a href="#">PODCAST</a><a href="#">VIDEOS</a><a href="#">BLOG</a><a href="#">CONTACT US</a>
      <svg width="14" height="14" viewBox="0 0 14 14"><circle cx="6" cy="6" r="4.5" fill="none" stroke="#fff" stroke-width="2"/><line x1="9.3" y1="9.3" x2="13" y2="13" stroke="#fff" stroke-width="2.2"/></svg>
    </nav>
  </div>
  <h1 class="hero-title">KINDRED ASCENT PARTNERS</h1>
  <p class="hero-sub">Physical, Spiritual, Financial, Leadership and Relationship goals</p>
  <div class="hero-btn">GET STARTED!</div>
  <div class="dots"><span class="on"></span><span></span><span></span><span></span></div>
</header>

<h2 class="section-title" style="top:626px">WELCOME TO KINDRED ASCENT PARTNERS</h2>
<p class="welcome-text">At vero eos et accusamus et iusto odio dignissimos ducimus qui blanditiis praesentium voluptatum deleniti atque corrupti quos dolores et quas molestias excepturi sint occaecati cupiditate non provident, similique sunt in culpa qui officia deserunt mollitia ani.</p>

<div class="pillar" style="left:71px">
  <div class="ring" style="border-color:var(--teal)"><svg width="50" height="46" viewBox="0 0 50 46"><path d="M25 44 C10 32 2 24 2 14 A11 11 0 0 1 25 8 A11 11 0 0 1 48 14 C48 24 40 32 25 44Z" fill="var(--teal)"/></svg></div>
  <h3>PHYSICAL</h3><p>Nam libero tempore, cum sol uta nobisest eligendi opti</p><span class="more" style="color:var(--teal)">READ MORE &gt;&gt;</span>
</div>
<div class="pillar" style="left:279px">
  <div class="ring" style="border-color:var(--green)"><svg width="54" height="52" viewBox="0 0 54 52" fill="none" stroke="var(--green)" stroke-width="3"><path d="M27 4 C40 16 34 30 27 30 C20 30 14 16 27 4Z"/><path d="M6 46 C8 30 20 26 27 30 C24 38 18 48 6 46Z"/><path d="M48 46 C46 30 34 26 27 30 C30 38 36 48 48 46Z"/></svg></div>
  <h3>SPIRITUAL</h3><p>Nam libero tempore, cum sol uta nobisest eligendi opti</p><span class="more" style="color:var(--green)">READ MORE &gt;&gt;</span>
</div>
<div class="pillar" style="left:488px">
  <div class="ring" style="border-color:var(--orange)"><svg width="56" height="36" viewBox="0 0 56 36"><rect x="1" y="1" width="54" height="34" fill="var(--orange)"/><rect x="6" y="6" width="44" height="24" fill="none" stroke="#fff" stroke-width="2"/><circle cx="28" cy="18" r="8" fill="#fff"/><text x="28" y="22" font-size="11" font-weight="700" text-anchor="middle" fill="var(--orange)" font-family="Open Sans,sans-serif">1</text></svg></div>
  <h3 style="color:var(--orange)">FINANCIAL</h3><p>Nam libero tempore, cum sol uta nobisest eligendi opti</p><span class="more" style="color:var(--teal)">READ MORE &gt;&gt;</span>
</div>
<div class="pillar" style="left:698px">
  <div class="ring" style="border-color:var(--blue)"><svg width="40" height="44" viewBox="0 0 40 44"><circle cx="20" cy="12" r="10" fill="var(--blue)"/><path d="M2 44 C2 30 10 25 20 25 C30 25 38 30 38 44Z" fill="var(--blue)"/></svg></div>
  <h3>LEADERSHIP</h3><p>Nam libero tempore, cum sol uta nobisest eligendi opti</p><span class="more" style="color:var(--blue)">READ MORE &gt;&gt;</span>
</div>
<div class="pillar" style="left:909px">
  <div class="ring" style="border-color:var(--red)"><svg width="44" height="44" viewBox="0 0 44 44"><circle cx="22" cy="22" r="20" fill="var(--red)"/><circle cx="22" cy="22" r="14" fill="#fff"/><circle cx="22" cy="22" r="9" fill="var(--red)"/><circle cx="22" cy="22" r="4" fill="#fff"/></svg></div>
  <h3>RELATIONSHIP GOALS</h3><p>Nam libero tempore, cum sol uta nobisest eligendi opti</p><span class="more" style="color:var(--red)">READ MORE &gt;&gt;</span>
</div>

<section class="stats" role="img" aria-label="Photo of hands typing on a laptop in warm sunset light">
  <div class="stat" style="left:112px"><div class="ring"><svg width="56" height="52" viewBox="0 0 56 52" fill="none" stroke="#fff" stroke-width="5"><path d="M6 36 V28 A22 22 0 0 1 50 28 V36"/><rect x="4" y="30" width="10" height="18" rx="3" fill="#fff"/><rect x="42" y="30" width="10" height="18" rx="3" fill="#fff"/></svg></div><div class="stat-num">1,528584</div><div class="stat-label">PODCAST LISTENS</div></div>
  <div class="stat" style="left:362px"><div class="ring"><svg width="64" height="48" viewBox="0 0 64 48" fill="#fff"><circle cx="32" cy="12" r="9"/><path d="M18 46 C18 30 24 24 32 24 C40 24 46 30 46 46Z"/><circle cx="13" cy="16" r="7"/><path d="M1 42 C1 30 6 26 13 26 C17 26 19 27 20 29 C17 33 16 37 16 42Z"/><circle cx="51" cy="16" r="7"/><path d="M63 42 C63 30 58 26 51 26 C47 26 45 27 44 29 C47 33 48 37 48 42Z"/></svg></div><div class="stat-num">863,800</div><div class="stat-label">ACTIVE USERS</div></div>
  <div class="stat" style="left:612px"><div class="ring"><svg width="64" height="44" viewBox="0 0 64 44" fill="none" stroke="#fff" stroke-width="4"><rect x="10" y="3" width="44" height="30" rx="2"/><path d="M2 40 H62"/></svg></div><div class="stat-num">63,800</div><div class="stat-label">ONLINE COURSES</div></div>
  <div class="stat" style="left:864px"><div class="ring"><svg width="40" height="56" viewBox="0 0 40 56" fill="none" stroke="#fff" stroke-width="4"><rect x="12" y="2" width="16" height="30" rx="8" fill="#fff"/><path d="M4 26 A16 16 0 0 0 36 26"/><path d="M20 42 V54"/></svg></div><div class="stat-num">3,863,800</div><div class="stat-label">KEYNOTE SPEECHES</div></div>
</section>

<h2 class="section-title" style="top:1512px">LATEST BLOG</h2>

<article class="card" style="left:98px;top:1579px">
  <div class="photo" role="img" aria-label="Photo of a woman in a yoga lunge by the sea" style="background:linear-gradient(180deg,#a9c3da,#8fa9bd 60%,#4d5560)"></div>
  <span class="tag">VIDEO</span>
  <svg class="play" width="60" height="60" viewBox="0 0 60 60"><circle cx="30" cy="30" r="28" fill="rgba(0,0,0,.55)" stroke="#fff" stroke-width="2"/><path d="M24 18 L42 30 L24 42Z" fill="#fff"/></svg>
  <h4>Finibus Bonorum Malorum</h4><div class="meta">&#9635; 03/05/2017 &nbsp;|&nbsp; &#9679; Ellis Harrow</div>
  <p class="excerpt">Nam libero tempore, cum soluta nobis est elige ndi optio cumque nihil impedit quo minus id qu od maxime placeat facere poss.</p><span class="more">READ MORE &gt;&gt;</span>
</article>
<article class="card" style="left:443px;top:1579px">
  <div class="photo" role="img" aria-label="Photo of a person meditating on grass in sunlight" style="background:linear-gradient(160deg,#e7e08a,#b8cf62 45%,#6f9a36 75%,#d45b7a)"></div>
  <span class="tag">POSCAST</span>
  <svg class="audio" width="110" height="50" viewBox="0 0 110 50" fill="#fff"><path d="M2 18 H10 L22 8 V42 L10 32 H2Z"/><rect x="34" y="20" width="3" height="10"/><rect x="42" y="12" width="3" height="26"/><rect x="50" y="6" width="3" height="38"/><rect x="58" y="14" width="3" height="22"/><rect x="66" y="8" width="3" height="34"/><rect x="74" y="16" width="3" height="18"/><rect x="82" y="20" width="3" height="10"/></svg>
  <h4>Finibus Bonorum Malorum</h4><div class="meta">&#9635; 03/05/2017 &nbsp;|&nbsp; &#9679; Ellis Harrow</div>
  <p class="excerpt">Nam libero tempore, cum soluta nobis est elige ndi optio cumque nihil impedit quo minus id qu od maxime placeat facere poss.</p><span class="more">READ MORE &gt;&gt;</span>
</article>
<article class="card" style="left:785px;top:1579px">
  <div class="photo" role="img" aria-label="Photo of a hand working over financial charts and a calculator" style="background:linear-gradient(135deg,#6a6f78,#c9ccd2 40%,#e8e8ea 70%,#b4a394)"></div>
  <span class="tag">VIDEO</span>
  <svg class="play" width="60" height="60" viewBox="0 0 60 60"><circle cx="30" cy="30" r="28" fill="rgba(0,0,0,.55)" stroke="#fff" stroke-width="2"/><path d="M24 18 L42 30 L24 42Z" fill="#fff"/></svg>
  <h4>Finibus Bonorum Malorum</h4><div class="meta">&#9635; 03/05/2017 &nbsp;|&nbsp; &#9679; Ellis Harrow</div>
  <p class="excerpt">Nam libero tempore, cum soluta nobis est elige ndi optio cumque nihil impedit quo minus id qu od maxime placeat facere poss.</p><span class="more">READ MORE &gt;&gt;</span>
</article>

<article class="card" style="left:98px;top:2034px">
  <div class="photo" role="img" aria-label="Photo of a businesswoman among glass office towers" style="background:linear-gradient(170deg,#8ea4b4,#b9c4c6 40%,#9a8d72 70%,#5f5a4f)"></div>
  <span class="tag">POSCAST</span>
  <svg class="audio" width="110" height="50" viewBox="0 0 110 50" fill="#fff"><path d="M2 18 H10 L22 8 V42 L10 32 H2Z"/><rect x="34" y="20" width="3" height="10"/><rect x="42" y="12" width="3" height="26"/><rect x="50" y="6" width="3" height="38"/><rect x="58" y="14" width="3" height="22"/><rect x="66" y="8" width="3" height="34"/><rect x="74" y="16" width="3" height="18"/><rect x="82" y="20" width="3" height="10"/></svg>
  <h4>Finibus Bonorum Malorum</h4><div class="meta">&#9635; 03/05/2017 &nbsp;|&nbsp; &#9679; Ellis Harrow</div>
  <p class="excerpt">Nam libero tempore, cum soluta nobis est elige ndi optio cumque nihil impedit quo minus id qu od maxime placeat facere poss.</p><span class="more">READ MORE &gt;&gt;</span>
</article>
<article class="card" style="left:443px;top:2034px">
  <div class="photo" role="img" aria-label="Photo of silhouetted figures joining puzzle pieces at sunset" style="background:linear-gradient(180deg,#6c4a3a,#d98a3e 45%,#f2b25a 60%,#3a2a22)"></div>
  <span class="tag">VIDEO</span>
  <svg class="play" width="60" height="60" viewBox="0 0 60 60"><circle cx="30" cy="30" r="28" fill="rgba(0,0,0,.55)" stroke="#fff" stroke-width="2"/><path d="M24 18 L42 30 L24 42Z" fill="#fff"/></svg>
  <h4>Finibus Bonorum Malorum</h4><div class="meta">&#9635; 03/05/2017 &nbsp;|&nbsp; &#9679; Ellis Harrow</div>
  <p class="excerpt">Nam libero tempore, cum soluta nobis est elige ndi optio cumque nihil impedit quo minus id qu od maxime placeat facere poss.</p><span class="more">READ MORE &gt;&gt;</span>
</article>
<article class="card" style="left:785px;top:2034px">
  <div class="photo" role="img" aria-label="Photo of chess pieces silhouetted against a blue dusk sky" style="background:linear-gradient(180deg,#4b6d8e,#8aa2b3 55%,#2a3038)"></div>
  <span class="tag">POSCAST</span>
  <svg class="audio" width="110" height="50" viewBox="0 0 110 50" fill="#fff"><path d="M2 18 H10 L22 8 V42 L10 32 H2Z"/><rect x="34" y="20" width="3" height="10"/><rect x="42" y="12" width="3" height="26"/><rect x="50" y="6" width="3" height="38"/><rect x="58" y="14" width="3" height="22"/><rect x="66" y="8" width="3" height="34"/><rect x="74" y="16" width="3" height="18"/><rect x="82" y="20" width="3" height="10"/></svg>
  <h4>Finibus Bonorum Malorum</h4><div class="meta">&#9635; 03/05/2017 &nbsp;|&nbsp; &#9679; Ellis Harrow</div>
  <p class="excerpt">Nam libero tempore, cum soluta nobis est elige ndi optio cumque nihil impedit quo minus id qu od maxime placeat facere poss.</p><span class="more">READ MORE &gt;&gt;</span>
</article>

<div class="view-more">VIEW MORE BLOG</div>

<footer>
  <div class="footer-rule"></div>
  <div class="footer-logo">Kindred Ascent Partners</div>
  <div class="fcol" style="left:350px">
    <h4>Quick Links</h4>
    <ul><li>About Us</li><li>Contact Us</li><li>Terms and Conditions</li><li>Privacy Policy</li><li>FAQ</li></ul>
  </div>
  <div class="fcol" style="left:557px;width:270px">
    <h4>Newsletter Subscription</h4>
    <p>Register your Email Address to get information about us</p>
    <div class="field">Email Address</div>
    <div class="subscribe">SUBSCRIBE</div>
  </div>
  <div class="fcol" style="left:885px;width:220px">
    <h4>Contact Us</h4>
    <div class="contact-row"><svg width="12" height="16" viewBox="0 0 12 16"><path d="M6 0 A6 6 0 0 1 12 6 C12 10 6 16 6 16 C6 16 0 10 0 6 A6 6 0 0 1 6 0Z" fill="var(--gold)"/><circle cx="6" cy="6" r="2.2" fill="#fff"/></svg><span>27 Linden Court, 12 Orchard Row, Ashby, AB1 2CD</span></div>
    <div class="contact-row"><svg width="14" height="14" viewBox="0 0 14 14"><path d="M3 0 L5.5 3.5 L4 5.5 C5 7.5 6.5 9 8.5 10 L10.5 8.5 L14 11 L12 14 C5 13 1 9 0 2Z" fill="var(--gold)"/></svg><span>1 555 010 2040</span></div>
    <div class="contact-row"><svg width="15" height="11" viewBox="0 0 15 11"><rect width="15" height="11" fill="var(--gold)"/><path d="M0 0 L7.5 6 L15 0" fill="none" stroke="#fff" stroke-width="1.3"/></svg><span>hello@kindredascent.example</span></div>
  </div>
  <div class="footer-bottom"></div>
  <p class="copyright">Copyright © 2017, Kindred Ascent Partners . All rights reserved.</p>
  <div class="socials"><span></span><span></span><span></span><span></span></div>
</footer>

</body>
</html>
```